BPX Van Wrap for Printing Business

I need a fill wrap that is professional and sleek. I want it to stand out but not be so cluttered and full of stuff that it looks stupid. I uploaded 3 designs from the wrap guy that are childish and cartoonish. Really just took some existing stuff and threw it together. Looks stupid and phallic to me. I uploaded his 3 designs which are bad (1 being the best of them), my logo, Van template, actual photos of the van and a photo I grabbed on google of a Vomarix Van which is simple and cool. I don't mind textures and backgrounds but I don't want it to look like a 10 year old made in in Canva.
I need my address and phone number on door as per the law for commercial vehicles.
As far as the rest of the van, phone number is not important, just the domain.
On my logo sheet are a few services we offer that I would like on the design.
Industry/Entity Type
Digital Printing and Wide Format Printing

```html
<!DOCTYPE html>
<html lang="en">
<head>
<meta charset="utf-8">
<title>Halden Press – Van Wrap</title>
<link href="https://fonts.googleapis.com/css2?family=Archivo+Black&family=Open+Sans:wght@400;600&display=swap" rel="stylesheet">
<style>
  :root{
    --navy:#2f3644;
    --navy-deep:#262c38;
    --blue:#1e9ad6;
    --grey:#cdd0d4;
    --glass:#3b4350;
    --ground:#eceef1;
  }
  html,body{margin:0;padding:0;overflow:hidden;}
  body{width:1185px;height:1200px;background:var(--ground);}
  .wrap-layout{display:block;width:1185px;height:1200px;}
  .body-blue{fill:var(--blue);}
  .body-navy{fill:var(--navy);}
  .rear-panel{fill:var(--navy-deep);}
  .sweep{fill:var(--blue);}
  .ring{fill:none;stroke:var(--grey);stroke-opacity:.55;stroke-width:14;}
  .glass{fill:var(--glass);}
  .arch{fill:var(--ground);}
  .seam{stroke:#1c2029;stroke-width:3;}
  .brand{font-family:"Archivo Black",sans-serif;fill:var(--grey);}
  .copy{font-family:"Open Sans",sans-serif;font-weight:600;fill:var(--grey);}
  .copy-blue{fill:var(--blue);}
  .mark-name{font-family:"Open Sans",sans-serif;font-weight:600;fill:var(--grey);}
</style>
</head>
<body>
<svg class="wrap-layout" viewBox="0 0 1185 1200" xmlns="http://www.w3.org/2000/svg">
  <defs>
    <path id="van-side-outline" d="M50,110 Q50,92 70,92 L730,88 Q760,88 790,100 L960,230 Q1000,250 1060,262 L1120,275 Q1145,282 1145,310 L1145,405 Q1145,420 1130,420 L50,420 Q40,420 40,405 L40,120 Z"/>
    <clipPath id="side-clip"><use href="#van-side-outline"/></clipPath>
    <g id="van-side-panel">
      <use href="#van-side-outline" class="body-blue"/>
      <g clip-path="url(#side-clip)">
        <path class="body-navy" d="M0,0 L650,0 Q570,250 650,440 L0,440 Z"/>
        <path class="sweep" d="M30,430 Q90,325 165,300 Q130,365 160,430 Z"/>
        <circle class="ring" cx="570" cy="300" r="215"/>
      </g>
      <path class="glass" d="M765,108 L930,108 Q945,110 955,125 L955,215 L765,215 Z"/>
      <line class="seam" x1="440" y1="92" x2="440" y2="420"/>
      <line class="seam" x1="740" y1="90" x2="740" y2="420"/>
      <circle class="arch" cx="225" cy="425" r="82"/>
      <circle class="arch" cx="1000" cy="425" r="78"/>
    </g>
  </defs>

  <g class="side-driver" transform="translate(0,20)">
    <use href="#van-side-panel"/>
    <text class="brand" x="80" y="170" font-size="58">HALDEN</text>
    <text class="brand" x="80" y="232" font-size="58">PRESS</text>
    <text class="copy" x="80" y="272" font-size="18">44 Orchard Hill Rd Westbrook, NJ 07999</text>
    <text class="copy" x="455" y="128" font-size="20">Digital printing large format</text>
    <text class="copy" x="490" y="156" font-size="20">printing direct mail</text>
    <text class="copy" x="455" y="196" font-size="32">Custom finishing</text>
    <text class="mark-name" x="570" y="322" font-size="46" text-anchor="middle">HALDEN</text>
    <text class="copy" x="800" y="285" font-size="17" letter-spacing="1.5">HALDENPRESS.COM</text>
    <text class="copy" x="800" y="318" font-size="26">555.014.2738</text>
  </g>

  <g class="side-passenger">
    <use href="#van-side-panel" transform="translate(720,600) scale(-0.62,0.62)"/>
    <text class="copy" x="30" y="768" font-size="13" letter-spacing="1">HALDENPRESS.COM</text>
    <text class="copy" x="30" y="792" font-size="18">555.014.2738</text>
    <text class="mark-name" x="367" y="796" font-size="30" text-anchor="middle">HALDEN</text>
    <text class="copy" x="268" y="686" font-size="12">Digital printing large format</text>
    <text class="copy" x="282" y="702" font-size="12">printing direct mail</text>
    <text class="copy" x="268" y="727" font-size="20">Custom finishing</text>
    <text class="brand" x="455" y="700" font-size="36">HALDEN</text>
    <text class="brand" x="455" y="740" font-size="36">PRESS</text>
    <text class="copy" x="455" y="762" font-size="11">44 Orchard Hill Rd Westbrook, NJ 07999</text>
  </g>

  <g class="rear-doors">
    <clipPath id="rear-clip"><rect x="770" y="610" width="380" height="520" rx="28"/></clipPath>
    <rect class="rear-panel" x="770" y="610" width="380" height="520" rx="28"/>
    <g clip-path="url(#rear-clip)">
      <path class="sweep" d="M770,1130 L770,960 Q840,1010 850,1130 Z"/>
      <path class="sweep" d="M1150,1130 L1150,950 Q1075,1010 1065,1130 Z"/>
    </g>
    <rect class="glass" x="790" y="630" width="162" height="150" rx="10" opacity=".55"/>
    <rect class="glass" x="968" y="630" width="162" height="150" rx="10" opacity=".55"/>
    <line class="seam" x1="960" y1="612" x2="960" y2="1128"/>
    <circle class="ring" cx="850" cy="700" r="58" stroke-width="5"/>
    <text class="mark-name" x="850" y="708" font-size="22" text-anchor="middle">HALDEN</text>
    <text class="copy" x="925" y="680" font-size="12">Digital printing large format</text>
    <text class="copy" x="940" y="696" font-size="12">printing direct mail</text>
    <text class="copy copy-blue" x="925" y="722" font-size="18">Custom finishing</text>
    <text class="copy" x="880" y="800" font-size="11">44 Orchard Hill Rd Westbrook, NJ 07999</text>
    <text class="brand" x="800" y="860" font-size="44">HALDEN</text>
    <text class="brand" x="800" y="912" font-size="44">PRESS</text>
    <text class="copy copy-blue" x="800" y="960" font-size="18" letter-spacing="1">HALDENPRESS.COM</text>
    <text class="copy" x="830" y="1000" font-size="28">555.014.2738</text>
  </g>
</svg>
</body>
</html>
```